dentist office tri-fold for root canal specialist

design a tri fold brochure to give to patients talking about the office and the services
Talk about doctors and their bios
services: root canal , retreatments, endodontic surgery, trauma, cracked teeth
Technology: CBCT, microscopes, lasers, soft tide advanced
I will provide all the technical info. willing to hire a writer if needed. Attached a picture of our logo as a reference of our colors. Can attach older versions of brochure if requested. Looking for a very professional tri fold that will be used to market the practice to patients and other doctors.
Rough idea: TRIFOLD
Front Cover:
Welcome to The Pulpwell Clinic
Thank you for allowing us to care for your endodontic needs. We look forward to serving you.
We at The Pulpwell Clinic have dedicated our professional lives to improving the comfort and dental health of those in our care.
Inner Right:
Pics of Docs
Welcome – On behalf of our staff, we welcome you to our office.
We are pleased that you have selected our team of professionals to care for your endodontic needs. We want you to know that we are committed to providing you, our patient with the highest quality endodontic care in the most gentle, efficient, and caring manner possible. We pride ourselves on offering our expertise along with the best patient care with the most up to date technologies to better ensure your oral health.
For your convenience, please visit us online at www.pulpwellclinic.example for directions to our offices, pre and post-operative instructions, general information on our Endodontists and much more. We are here for you and our doctors are on call 24 hours a day, 7 days a week.
We are looking forward providing you a most relaxed and pleasant vist possible. Thank you again for choosing The Pulpwell Clinic.
Inner Middle:
What is a Root Canal?
A root canal (endodontic treatment) is one of the most common dental procedures performed, with more than 14 million performed every year. This simple treatment can save your natural teeth and prevent the need of dental implants or bridges.
At the center of your tooth is pulp. The pulp is a collection of blood vessels, nerves and lymphatics, which help to form the tooth during the stages of tooth development.
I’ve already had a root canal, why do I need another procedure?
Retreatment - A second chance to save your tooth
With proper care, most teeth which have had endodontic (root canal) treatment can last as long as other natural teeth.
However, in a few cases, a tooth that has received endodontic treatment fails to heal completely. And occasionally, a tooth becomes painful or diseased months or even years after previously successful endodontic treatment.
If your tooth has failed to heal or has developed new problems, you have a second chance. Another endodontic procedure, called retreatment, may be able to save your tooth.
Retreated teeth can function well for years, even for a lifetime. It's always best to save the tooth if your endodontist believes retreatment is the best option for you.
Advances in technology are constantly changing the way root canal treatment is performed, so your endodontist may even be able to use a new technique that was not available when you had your first procedure.
Of course, there are no guarantees with any dental or medical procedure. Your endodontist will discuss your options and the chances of success before beginning retreatment.
What is an Apicoectomy?
In this procedure, the endodontist opens the gum tissue near the tooth to see the underlying bone and to remove any inflamed or infected tissue. The very end of the root is also removed or resected.
Inner Right:
Patient Care: Needing a root canal is often a surprise and sometimes an emergency. We at The Pulpwell Clinic make certain that every patient receives prompt emergency care at any time.
We understand how uneasy some patients may feel about dental visits and how we can make a difference in providing a relaxing, positive experience. Our doctors are trained in different levels of sedation dentistry from Nitrous Oxide to Conscious Sedation.
Our entire team is dedicated to providing you with excellent, personalized care and service to make your visit as comfortable and pleasant as possible. You will enjoy our relaxing treatment rooms, complete with plushform coverings, televisions and Tunelets for your use during treatment and blankets to keep you warm if you’re cold.
Technical Equipment: The Pulpwell Clinic prides itself in utilizing the most advanced techniques and state-of-the-art equipment including digital radiography, fiber optic illumination, ultrasonic equipment, and operating microscopes, which help the doctor see microscopic details inside a tooth during micro-surgical and non-surgical procedures.
Expertise: The Pulpwell Clinic is staffed by doctors who are responsive to your concerns and alert to your experience during treatment. All of our doctors are endodontists, which means they are specialists who have completed 2-3 years of advanced training in addition to dental school. We are all specialist members of the National Council of Rootcare Dentists (NCRD). All our endodontists continue their education and training through professional associations, seminars, study groups, and teaching both at Brindlemoor and Carraway Universities.

```html
<!DOCTYPE html>
<html lang="en">
<head>
<meta charset="utf-8">
<title>The Pulpwell Clinic – Tri-fold Brochure</title>
<link href="https://fonts.googleapis.com/css2?family=Open+Sans:ital,wght@0,400;0,600;0,700;1,400;1,700&display=swap" rel="stylesheet">
<style>
:root{
  --lavender:#6f76a8;
  --navy:#1e2a66;
  --ink:#2a3270;
  --paper:#ffffff;
  --stage:#eceef3;
  --photo-a:#c9ccd3;
  --photo-b:#e9ebef;
}
*{box-sizing:border-box;margin:0;padding:0}
html,body{width:1200px;height:1000px;overflow:hidden}
body{background:var(--stage);font-family:"Open Sans",Arial,sans-serif;color:var(--ink);position:relative}
.spread{position:absolute;left:280px;width:640px;height:485px;display:grid;grid-template-columns:repeat(3,1fr);background:var(--paper);box-shadow:0 2px 8px rgba(0,0,0,.18)}
.spread--outside{top:8px}
.spread--inside{top:505px}
.panel{position:relative;overflow:hidden;font-size:7.4px;line-height:1.38}
.panel--lavender{background:var(--lavender);color:#fff}
.photo{background:linear-gradient(160deg,var(--photo-b),var(--photo-a))}
p{margin-bottom:7px}
.justify p{text-align:justify}

/* outside left */
.team-photo{height:140px}
.welcome{padding:12px 18px 0}
.welcome h2{font-size:10px;line-height:1.3;font-weight:700;color:var(--navy);margin-bottom:9px}
.welcome h2 em{font-style:italic}
.footer-bar{position:absolute;left:18px;right:18px;bottom:0;height:24px;background:var(--lavender)}

/* contact */
.contact-frame{position:absolute;left:14px;right:14px;top:20px;bottom:18px;border:1px solid #fff;text-align:center;padding:0 8px}
.contact-title{position:absolute;top:-9px;left:50%;transform:translateX(-50%);background:var(--lavender);padding:0 8px;font-size:13px;font-weight:700;letter-spacing:.5px;white-space:nowrap}
.office{margin-top:30px}
.office + .office{margin-top:24px}
.office h3{font-size:8.4px;font-weight:700;color:var(--navy);margin-bottom:10px}
.office .item{margin-bottom:9px}
.office svg{display:block;margin:0 auto 3px;width:9px;height:9px}
.web{position:absolute;bottom:22px;left:0;right:0;font-size:6.6px}
.web strong{display:block;font-weight:700}

/* cover */
.cover-frame{position:absolute;left:8px;right:8px;top:6px;height:370px;border:1px solid var(--navy)}
.cover-photo{position:absolute;left:0;right:0;top:0;height:300px}
.brand{position:absolute;left:22px;top:330px;display:flex;align-items:center;gap:6px;font-size:11px;font-weight:600;color:var(--navy)}
.brand i{display:block;width:10px;height:10px;border-radius:50%;background:var(--navy)}
.cover-band{position:absolute;left:0;right:0;bottom:16px;height:76px;background:var(--lavender);padding:14px 14px 0 22px;font-style:italic;font-size:8px;line-height:1.75;color:#fff}

/* inside left */
.info-box{margin:22px 12px 0;border:1px solid var(--navy);padding:12px 14px 10px}
.info-box h2,.panel h2{font-size:10px;font-weight:700;color:var(--navy);margin-bottom:9px;line-height:1.3}
.info-box p{font-size:8.2px;line-height:1.42;color:var(--ink)}
.exam-photo{position:absolute;left:0;right:0;bottom:0;height:220px}

/* inside middle */
.retreat{padding:14px 14px 0 16px;font-size:6.9px;line-height:1.36}
.retreat p{margin-bottom:6px}
.retreat h2{margin-top:2px}
.mid-bar{position:absolute;left:16px;right:14px;bottom:0;height:10px;background:var(--lavender)}

/* inside right */
.services{padding:10px 12px 0 10px;font-size:6.9px;line-height:1.36}
.services p{margin-bottom:6px}
.services h3{display:flex;align-items:center;gap:6px;font-size:8.4px;font-weight:700;color:var(--navy);margin:8px 0 3px;white-space:nowrap}
.services h3::before{content:"";flex:1;height:1px;background:#fff}
.services h3:first-child{margin-top:0}
</style>
</head>
<body>

<section class="spread spread--outside">
  <article class="panel panel--welcome">
    <div class="photo team-photo" role="img" aria-label="Group portrait of the clinic's doctors and staff in white coats"></div>
    <div class="welcome justify">
      <h2><em>Welcome</em> – On behalf of our staff, we welcome you to our office.</h2>
      <p>We are pleased that you have selected our team of professionals to care for your endodontic needs. We want you to know that we are committed to providing you, our patient with the highest quality endodontic care in the most gentle, efficient, and caring manner possible. We pride ourselves on offering our expertise along with the best patient care with the most up to date technologies to better ensure your oral health.</p>
      <p>For your convenience, please visit us online at www.pulpwellclinic.example for directions to our offices, pre and post-operative instructions, general information on our Endodontists and much more. We are here for you and our doctors are on call 24 hours a day, 7 days a week.</p>
      <p>We are looking forward providing you a most relaxed and pleasant visit possible. Thank you again for choosing The Pulpwell Clinic.</p>
    </div>
    <div class="footer-bar"></div>
  </article>

  <article class="panel panel--lavender panel--contact">
    <div class="contact-frame">
      <div class="contact-title">CONTACT US</div>
      <div class="office">
        <h3>ASHBOURNE OFFICE</h3>
        <div class="item"><svg viewBox="0 0 10 10"><path d="M5 0a3.5 3.5 0 0 0-3.5 3.5C1.5 6 5 10 5 10s3.5-4 3.5-6.5A3.5 3.5 0 0 0 5 0zm0 5a1.4 1.4 0 1 1 0-2.8A1.4 1.4 0 0 1 5 5z" fill="#fff"/></svg>55 Orchard Street<br>Ashbourne, MA 01990</div>
        <div class="item"><svg viewBox="0 0 10 10"><path d="M2 0.5l2 2-1 1.3c.6 1.3 1.6 2.3 2.9 2.9L7.2 5.7l2 2-1.3 1.8C4 9 1 6 .5 2z" fill="#fff"/></svg>555-010-4821</div>
        <div class="item"><svg viewBox="0 0 10 10"><path d="M2 0.5l2 2-1 1.3c.6 1.3 1.6 2.3 2.9 2.9L7.2 5.7l2 2-1.3 1.8C4 9 1 6 .5 2z" fill="#fff"/></svg>555-010-7734</div>
        <div class="item"><svg viewBox="0 0 10 10"><circle cx="5" cy="5" r="4.6" fill="#fff"/><path d="M5 2.2V5h2" stroke="#6f76a8" stroke-width="1" fill="none"/></svg>Monday - Friday | 8:30 am – 5:30 pm<br>Saturday | 9:00 am – 2:00 pm</div>
      </div>
      <div class="office">
        <h3>LARKMOOR OFFICE</h3>
        <div class="item"><svg viewBox="0 0 10 10"><path d="M5 0a3.5 3.5 0 0 0-3.5 3.5C1.5 6 5 10 5 10s3.5-4 3.5-6.5A3.5 3.5 0 0 0 5 0zm0 5a1.4 1.4 0 1 1 0-2.8A1.4 1.4 0 0 1 5 5z" fill="#fff"/></svg>16 Harbor Lane<br>Larkmoor, MA 01985</div>
        <div class="item"><svg viewBox="0 0 10 10"><path d="M2 0.5l2 2-1 1.3c.6 1.3 1.6 2.3 2.9 2.9L7.2 5.7l2 2-1.3 1.8C4 9 1 6 .5 2z" fill="#fff"/></svg>555-010-3360</div>
        <div class="item"><svg viewBox="0 0 10 10"><path d="M2 0.5l2 2-1 1.3c.6 1.3 1.6 2.3 2.9 2.9L7.2 5.7l2 2-1.3 1.8C4 9 1 6 .5 2z" fill="#fff"/></svg>555-010-9172</div>
        <div class="item"><svg viewBox="0 0 10 10"><circle cx="5" cy="5" r="4.6" fill="#fff"/><path d="M5 2.2V5h2" stroke="#6f76a8" stroke-width="1" fill="none"/></svg>Monday - Friday | 8:30 am – 5:30 pm<br>Saturday | Closed</div>
      </div>
      <div class="web"><strong>CHECK OUR WEBSITE FOR MORE INFO</strong>www.pulpwellclinic.example</div>
    </div>
  </article>

  <article class="panel panel--cover">
    <div class="cover-frame">
      <div class="photo cover-photo" role="img" aria-label="Endodontist treating a patient under an operating microscope"></div>
      <div class="brand"><i></i>The Pulpwell Clinic</div>
    </div>
    <div class="cover-band">We at The Pulpwell Clinic have dedicated our professional lives to improving the comfort and dental health of those in our care.</div>
  </article>
</section>

<section class="spread spread--inside">
  <article class="panel panel--rootcanal">
    <div class="info-box">
      <h2>What is a Root Canal?</h2>
      <p>A root canal (endodontic treatment) is one of the most common dental procedures performed, with more than 14 million performed every year. This simple treatment can save your natural teeth and prevent the need of dental implants or bridges.</p>
      <p>At the center of your tooth is pulp. The pulp is a collection of blood vessels, nerves and lymphatics, which help to form the tooth during the stages of tooth development.</p>
    </div>
    <div class="photo exam-photo" role="img" aria-label="Doctor reviewing dental x-rays on a monitor with a seated patient"></div>
  </article>

  <article class="panel panel--retreatment">
    <div class="retreat">
      <h2>I’ve already had a root canal, why do I need another procedure?</h2>
      <p>Retreatment - A second chance to save your tooth. With proper care, most teeth which have had endodontic (root canal) treatment can last as long as other natural teeth.</p>
      <p>However, in a few cases, a tooth that has received endodontic treatment fails to heal completely. And occasionally, a tooth becomes painful or diseased months or even years after previously successful endodontic treatment.</p>
      <p>If your tooth has failed to heal or has developed new problems, you have a second chance. Another endodontic procedure, called retreatment, may be able to save your tooth.</p>
      <p>Retreated teeth can function well for years, even for a lifetime. It's always best to save the tooth if your endodontist believes retreatment is the best option for you.</p>
      <p>Advances in technology are constantly changing the way root canal treatment is performed, so your endodontist may even be able to use a new technique that was not available when you had your first procedure.</p>
      <p>Of course, there are no guarantees with any dental or medical procedure. Your endodontist will discuss your options and the chances of success before beginning retreatment.</p>
      <h2>What is an Apicoectomy?</h2>
      <p>In this procedure, the endodontist opens the gum tissue near the tooth to see the underlying bone and to remove any inflamed or infected tissue. The very end of the root is also removed or resected.</p>
    </div>
    <div class="mid-bar"></div>
  </article>

  <article class="panel panel--lavender panel--services">
    <div class="services justify">
      <h3>Patient Care</h3>
      <p style="text-align:center">Needing a root canal is often a surprise and sometimes an emergency. We at The Pulpwell Clinic make certain that every patient receives prompt emergency care at any time.</p>
      <p>We understand how uneasy some patients may feel about dental visits and how we can make a difference in providing a relaxing, positive experience. Our doctors are trained in different levels of sedation dentistry from Nitrous Oxide to Conscious Sedation.</p>
      <p>Our entire team is dedicated to providing you with excellent, personalized care and service to make your visit as comfortable and pleasant as possible. You will enjoy our relaxing treatment rooms, complete with plushform coverings, televisions and Tunelets for your use during treatment and blankets to keep you warm if you’re cold.</p>
      <h3>Technical Equipment</h3>
      <p>The Pulpwell Clinic prides itself in utilizing the most advanced techniques and state-of-the-art equipment including digital radiography, fiber optic illumination, ultrasonic equipment, and operating microscopes, which help the doctor see microscopic details inside a tooth during micro-surgical and non-surgical procedures.</p>
      <h3>Expertise</h3>
      <p>The Pulpwell Clinic is staffed by doctors who are responsive to your concerns and alert to your experience during treatment. All of our doctors are endodontists, which means they are specialists who have completed 2-3 years of advanced training in addition to dental school. We are all specialist members of the National Council of Rootcare Dentists (NCRD). All our endodontists continue their education and training through professional associations, seminars, study groups, and teaching both at Brindlemoor and Carraway Universities.</p>
    </div>
  </article>
</section>

</body>
</html>
```